Business Card for TVK, logo files already created

Please, can you assist with creating a Business card the TVK graphics which are already listed on www.brinmoretech.example
The business card should be modern and upmarket, textured designs are welcome. Please feel free to express yourself and be very bold with your design.

Target Market(s)

Cyber Security

Industry/Entity Type

Information Technology

Contact Information for Business Card

Company Name
Name
Title
Mobile
Fax or Tel
email
url

Font styles to use
Serif
Sans Serif

Colors
3277b5
85acd3
ffffff

```html
<!DOCTYPE html>
<html lang="en">
<head>
<meta charset="utf-8">
<title>TVK Business Card</title>
<link rel="stylesheet" href="https://fonts.googleapis.com/css2?family=Archivo:wght@400;700;900&display=swap">
<style>
  :root {
    --navy: #1e3a9c;
    --navy-deep: #17308a;
    --navy-light: #2f52b8;
    --white: #ffffff;
    --steel: #4a4f58;
    --stage: #2a2c31;
    --ink-soft: #d9e2f5;
  }
  * { margin: 0; padding: 0; box-sizing: border-box; }
  html, body { width: 1200px; height: 800px; overflow: hidden; }
  body {
    background: var(--stage);
    font-family: "Archivo", Arial, sans-serif;
    position: relative;
  }
  .card {
    position: absolute;
    width: 520px;
    height: 300px;
    overflow: hidden;
    box-shadow: 0 14px 30px rgba(0,0,0,0.45);
  }
  /* Front */
  .card-front { left: 50px; top: 250px; background: var(--navy); }
  .front-texture {
    position: absolute; inset: 0;
    background: linear-gradient(135deg, var(--navy-deep) 0%, var(--navy) 55%, var(--navy-light) 100%);
  }
  .front-name {
    position: absolute; right: 48px; top: 120px;
    font-size: 64px; font-weight: 900; letter-spacing: 2px;
    color: #6f8fd6;
  }
  /* Back */
  .card-back { left: 630px; top: 250px; background: var(--navy); }
  .back-brand {
    position: absolute; left: 0; top: 0; bottom: 0; width: 218px;
    background: var(--white);
    display: flex; flex-direction: column; align-items: center; justify-content: center;
  }
  .brand-name { font-size: 58px; font-weight: 900; color: var(--navy); line-height: 1; }
  .brand-company {
    margin-top: 8px; font-size: 13px; font-weight: 900; color: var(--navy);
    letter-spacing: 0.5px; text-transform: uppercase;
  }
  .brand-rule { width: 160px; height: 1px; background: var(--steel); margin: 7px 0 5px; }
  .brand-tagline { font-size: 8px; font-weight: 700; color: var(--navy); letter-spacing: 0.6px; text-transform: uppercase; }
  .back-info { position: absolute; left: 218px; top: 0; right: 0; bottom: 0; }
  .back-sheen { position: absolute; inset: 0; }
  .contact { position: absolute; left: 42px; top: 58px; color: var(--white); }
  .person-name { font-size: 20px; font-weight: 900; text-transform: uppercase; letter-spacing: 0.5px; }
  .person-title { font-size: 12px; margin-top: 1px; }
  .address { font-size: 12px; line-height: 1.3; margin-top: 18px; }
  .contact-list { list-style: none; margin-top: 16px; font-size: 12px; }
  .contact-list li { display: flex; align-items: center; gap: 8px; margin-bottom: 5px; }
  .contact-list svg { width: 14px; height: 14px; flex: none; }
</style>
</head>
<body>
  <section class="card card-front">
    <div class="front-texture" role="img" aria-label="Repeating faint company lettering pattern in deep blue tones"></div>
    <div class="front-name">TVK</div>
  </section>

  <section class="card card-back">
    <div class="back-brand">
      <div class="brand-name">TVK</div>
      <div class="brand-company">Brinmore Tech Solutions</div>
      <div class="brand-rule"></div>
      <div class="brand-tagline">Intelligence-Driven Solutions</div>
    </div>
    <div class="back-info">
      <svg class="back-sheen" viewBox="0 0 302 300" preserveAspectRatio="none">
        <rect width="302" height="300" fill="#1e3a9c"/>
        <path d="M0 0 H302 V130 C220 90 120 40 0 20 Z" fill="#2a4cb3" opacity="0.6"/>
      </svg>
      <div class="contact">
        <div class="person-name">Alex Carter</div>
        <div class="person-title">CEO</div>
        <div class="address">PO Box 456 Harbor Lane<br>4th Street<br>Lakeview, USA</div>
        <ul class="contact-list">
          <li>
            <svg viewBox="0 0 14 14"><rect width="14" height="14" rx="3" fill="#fff"/><rect x="4.5" y="2.5" width="5" height="9" rx="1" fill="none" stroke="#1e3a9c" stroke-width="1.2"/></svg>
            555 010 0199
          </li>
          <li>
            <svg viewBox="0 0 14 14"><rect width="14" height="14" rx="3" fill="#fff"/><rect x="3" y="4" width="8" height="6" fill="none" stroke="#1e3a9c" stroke-width="1.1"/><path d="M3 4 L7 7.5 L11 4" fill="none" stroke="#1e3a9c" stroke-width="1.1"/></svg>
            info@brinmoretech.example
          </li>
          <li>
            <svg viewBox="0 0 14 14"><circle cx="7" cy="7" r="7" fill="#fff"/><circle cx="7" cy="7" r="4" fill="none" stroke="#1e3a9c" stroke-width="1.1"/><path d="M3 7 H11 M7 3 V11" stroke="#1e3a9c" stroke-width="1"/></svg>
            www.brinmoretech.example
          </li>
        </ul>
      </div>
    </div>
  </section>
</body>
</html>
```